Accounting & Tax Services in Edmonton, Canada-Needs Website Design & Improvement

I am starting my business for accounting and tax services in Canada. I have my website but not much happy with that. My services are for bookkeeping, accounting and tax services. We serve both individual and corporate clients. I am trying to bring new idea in the market for providing services at their facility or business. My existing website is www.kvrm.ca
Currently, this site is static but I want to improve it to dynamic or interactive in nature.

Target Market(s)

Edmonton and Surrounding Areas, Canada

Industry/Entity Type

Public Accounting

Logo Text

Lakeshore Ledger & Office Partners

Number of Pages Required

4 page

Font styles to use
Sans Serif

Colors

Designer to choose colors to be used in the design.

Requirements
Must have
• 4 Pages
• I a not sure what do we mean by coded and uncoded design. Need clarification
• Rest is explained in project description. It should have the ingredients to attract traffic in any professional website.
• Logo Design Text can be shortened, if required.
• Existing logo attached, just for reference.
Nice to have
• 5 Pages

```html
<!DOCTYPE html>
<html lang="en">
<head>
<meta charset="utf-8">
<title>Lakeshore Ledger</title>
<link href="https://fonts.googleapis.com/css2?family=Asap:wght@400;500;600;700&family=Open+Sans:wght@400;600;700&display=swap" rel="stylesheet">
<style>
:root{
  --teal:#2f6e8e;
  --teal-dark:#24546d;
  --ink:#2d3a42;
  --text:#5c6770;
  --muted:#8a949b;
  --line:#dfe3e6;
  --grey-bg:#ececec;
  --white:#ffffff;
  --panel:#2b2b2b;
}
*{box-sizing:border-box;margin:0;padding:0}
html,body{width:1200px;height:4663px;overflow:hidden}
body{font-family:"Open Sans",Arial,sans-serif;color:var(--text);background:var(--white);position:relative}
section,header,footer{position:absolute;left:0;width:1200px}
.abs{position:absolute}
.h2{font-family:"Asap",Arial,sans-serif;font-weight:700;font-size:40px;color:var(--ink);text-transform:uppercase;text-align:center;letter-spacing:.5px}
.h2 span{color:var(--teal)}
.dots{position:absolute;left:0;width:1200px;display:flex;justify-content:center;gap:8px}
.dots i{display:block;width:34px;height:4px;background:#cfd6da}
.dots i.on{background:var(--teal)}
.more{font-size:16px;font-weight:700;color:var(--teal);text-transform:uppercase}

/* header + hero */
.hero{top:0;height:668px;background:linear-gradient(135deg,#e3e8ec 0%,#cfd8de 45%,#e9edf0 100%)}
.hero-photo{position:absolute;inset:0;background:radial-gradient(ellipse at 30% 40%,rgba(180,195,205,.6),transparent 60%),radial-gradient(ellipse at 80% 60%,rgba(170,185,195,.5),transparent 55%)}
.site-header{top:0;height:115px;background:rgba(255,255,255,.88);border-bottom:1px solid var(--line);z-index:2}
.brand{position:absolute;left:78px;top:36px;display:flex;align-items:center;gap:12px;font-family:"Asap",Arial,sans-serif;font-weight:600;font-size:28px;color:var(--teal-dark);white-space:nowrap}
.brand i{display:block;width:26px;height:26px;background:var(--teal)}
.nav{position:absolute;left:372px;top:0;display:flex;height:115px}
.nav a{display:block;padding:48px 12px 0;font-size:17px;color:var(--teal);text-decoration:none;height:115px;white-space:nowrap}
.nav a.active{border-bottom:4px solid var(--teal)}
.hero-title{position:absolute;top:280px;width:1200px;text-align:center;font-family:"Asap",Arial,sans-serif;font-weight:700;font-size:74px;color:var(--teal)}
.hero-sub{position:absolute;top:382px;width:1200px;text-align:center;font-family:"Asap",Arial,sans-serif;font-size:34px;color:var(--teal)}
.hero-btns{position:absolute;top:436px;width:1200px;display:flex;justify-content:center;gap:14px}
.btn{display:block;height:48px;padding:0 30px;line-height:46px;font-size:20px;font-weight:700;text-transform:uppercase;font-family:"Asap",Arial,sans-serif}
.btn-solid{background:var(--teal);color:#fff;border:1px solid var(--teal)}
.btn-line{background:rgba(255,255,255,.7);color:var(--teal);border:2px solid var(--teal)}
.hero-dots{position:absolute;top:622px;width:1200px;display:flex;justify-content:center;gap:6px}
.hero-dots i{display:block;width:16px;height:16px;border-radius:50%;border:2px solid #777;background:#fff}
.hero-dots i.on{background:#555}

/* services */
.services{top:668px;height:538px;background:#fff}
.card{position:absolute;background:#fff;border:1px solid var(--line);box-shadow:0 2px 6px rgba(0,0,0,.08)}
.svc-card{top:118px;width:324px;height:343px;padding:14px}
.svc-img{height:190px;background:linear-gradient(135deg,#9fb4c4,#dfe6ec)}
.card h3{font-family:"Asap",Arial,sans-serif;font-weight:700;font-size:22px;color:var(--teal-dark);margin:18px 0 10px}
.card p{font-size:15px;line-height:1.55}

/* helping */
.helping{top:1206px;height:566px;background:var(--grey-bg)}
.helping-band{position:absolute;top:0;left:0;width:1200px;height:317px;background:linear-gradient(120deg,var(--teal-dark),var(--teal) 60%,#3d7f9f)}
.helping h2{position:absolute;top:86px;width:1200px;text-align:center;font-family:"Asap",Arial,sans-serif;font-weight:600;font-size:34px;color:#fff}
.helping .lead{position:absolute;top:138px;left:150px;width:900px;text-align:center;font-size:15px;line-height:1.55;color:#e5eef3}
.help-card{top:227px;width:324px;height:252px;padding:26px}
.help-card svg{display:block}
.help-card h3{margin-top:16px}

/* about */
.about{top:1772px;height:482px;background:var(--grey-bg)}
.about-img{position:absolute;left:78px;top:56px;width:500px;height:354px;background:linear-gradient(135deg,#3a4650,#8b98a2);border:10px solid #23292e}
.about-text{position:absolute;left:616px;top:86px;width:506px}
.about-text h2{font-family:"Asap",Arial,sans-serif;font-weight:700;font-size:40px;color:var(--ink);margin-bottom:12px;text-transform:uppercase}
.about-text h2 span{color:var(--teal)}
.about-text p{font-size:15px;line-height:1.6;margin-bottom:10px}

/* tax alerts */
.alerts{top:2254px;height:320px;background:#fff}
.alerts .h2{position:absolute;top:60px;width:1200px}
.alerts h3{position:absolute;top:126px;width:1200px;text-align:center;font-family:"Asap",Arial,sans-serif;font-weight:700;font-size:23px;color:var(--ink)}
.alerts p{position:absolute;top:168px;left:190px;width:820px;text-align:center;font-size:16px;line-height:1.6}

/* quote */
.quote{top:2574px;height:523px;background:#eef0f2}
.quote-img{position:absolute;right:0;top:0;width:610px;height:523px;background:linear-gradient(110deg,#eef0f2 0%,#a9bccb 30%,#3d5f86 70%,#2c4a6e 100%)}
.quote h2{position:absolute;left:78px;top:98px;font-family:"Asap",Arial,sans-serif;font-weight:700;font-size:40px;color:var(--ink);text-transform:uppercase}
.quote h2 span{color:var(--teal)}
.quote .lead{position:absolute;left:78px;top:164px;width:470px;font-size:15px;line-height:1.6}
.field{position:absolute;height:46px;width:220px;background:#fff;border:1px solid #cfd4d8;font-size:15px;color:#666;padding:12px 14px}
.submit{position:absolute;left:78px;top:368px;width:156px;height:46px;background:var(--teal);color:#fff;font-weight:700;font-size:18px;line-height:46px;text-align:center;font-family:"Asap",Arial,sans-serif}

/* team */
.team{top:3097px;height:559px;background:#fff}
.team .h2{position:absolute;top:42px;width:1200px}
.member{top:146px;width:324px;height:351px;padding:0}
.member-img{height:202px;background:linear-gradient(180deg,#e9edf0,#b4bfc7)}
.member h3{text-align:center;font-family:"Asap",Arial,sans-serif;font-weight:400;font-size:26px;color:var(--ink);margin:22px 0 14px}
.member hr{border:0;height:2px;background:var(--ink);width:110px;margin:0 auto 16px}
.member p{text-align:center;font-size:15px;line-height:1.5;padding:0 30px}

/* news */
.news{top:3656px;height:464px;background:var(--grey-bg)}
.news .title{position:absolute;top:64px;font-family:"Asap",Arial,sans-serif;font-weight:700;font-size:40px;color:var(--ink);text-transform:uppercase}
.news .title span{color:var(--teal)}
.post{top:149px;width:322px;height:243px;padding:44px 14px 0}
.post h3{margin:0 0 8px}
.post .meta{position:absolute;left:14px;right:14px;top:194px;display:flex;justify-content:space-between;font-size:14px}
.subscribe{position:absolute;left:799px;top:149px;width:323px;height:228px;background:var(--teal-dark);padding:30px 26px;color:#e8f0f4}
.subscribe p{font-size:15px;line-height:1.55;margin-bottom:14px}
.sub-field{height:40px;border:1px solid #7fa3b6;font-size:15px;padding:9px 12px;margin-bottom:12px;position:relative;background:rgba(255,255,255,.05)}
.sub-btn{position:absolute;right:-1px;top:-1px;width:52px;height:40px;border:1px solid #7fa3b6;display:flex;align-items:center;justify-content:center}

/* map */
.map{top:4120px;height:279px;background:linear-gradient(135deg,#d5dadf,#c2cad1 50%,#d9dee2)}
.office{position:absolute;left:78px;top:86px;width:342px;height:193px;background:var(--panel);padding:18px 22px;color:#eaeaea}
.office h3{font-family:"Asap",Arial,sans-serif;font-weight:500;font-size:22px;margin-bottom:8px}
.office li{list-style:none;display:flex;gap:12px;font-size:13px;line-height:1.45;margin-bottom:6px}
.office svg{flex:none;margin-top:2px}
.pin{position:absolute;left:490px;top:0}

/* footer */
.site-footer{top:4399px;height:264px;background:var(--teal)}
.foot-nav{position:absolute;left:78px;top:132px;display:flex;gap:30px}
.foot-nav a{color:#fff;font-size:16px;text-decoration:none;white-space:nowrap}
.social{position:absolute;left:978px;top:120px;display:flex;gap:10px}
.social i{display:block;width:40px;height:40px;border-radius:50%;background:#fff}
.foot-line{position:absolute;left:78px;top:180px;width:1044px;height:1px;background:rgba(255,255,255,.35)}
.copy{position:absolute;top:216px;width:1200px;text-align:center;font-size:15px;color:#fff}
.to-top{position:absolute;left:1134px;top:212px;width:54px;height:54px;border-radius:50%;border:2px solid #fff;display:flex;align-items:center;justify-content:center}
</style>
</head>
<body>

<section class="hero">
  <div class="hero-photo" role="img" aria-label="Background photo of a desk with tablet, documents and people working"></div>
  <div class="hero-title">Lakeshore Ledger</div>
  <div class="hero-sub">Your Success is our Business</div>
  <div class="hero-btns"><span class="btn btn-solid">Client Portal</span><span class="btn btn-line">Know More</span></div>
  <div class="hero-dots"><i></i><i></i><i></i><i class="on"></i></div>
</section>

<header class="site-header">
  <div class="brand"><i></i>Lakeshore Ledger</div>
  <nav class="nav">
    <a class="active">Home</a><a>About Us</a><a>Services</a><a>Newsletter</a><a>Financial Tools</a><a>Info Center</a><a>Contact</a>
  </nav>
</header>

<section class="services">
  <div class="h2 abs" style="top:48px;width:1200px">Our <span>Services</span></div>
  <div class="card svc-card" style="left:78px">
    <div class="svc-img" role="img" aria-label="Photo of a laptop and financial papers"></div>
    <h3>Bookkeeping</h3>
    <p>Meaningful, well organized financial records ensure that your business...</p>
    <div class="more">Know More</div>
  </div>
  <div class="card svc-card" style="left:438px">
    <div class="svc-img" role="img" aria-label="Photo of charts, calculator and pens on a desk"></div>
    <h3>Accounting</h3>
    <p>In order to guarantee our clients' success, we believe that it is necessary.</p>
    <div class="more">Know More</div>
  </div>
  <div class="card svc-card" style="left:798px">
    <div class="svc-img" role="img" aria-label="Photo of a calculator and tax forms"></div>
    <h3>Tax services</h3>
    <p>Our team recognizes how difficult it is to stay up-to-date on the dynamic tax.</p>
    <div class="more">Know More</div>
  </div>
</section>

<section class="helping">
  <div class="helping-band"></div>
  <h2>Helping both individual and corporate clients</h2>
  <p class="lead">Our firm offers a wide range of services to our individual and business clients. Our clients benefit from personalized, quality service that is beyond comparison. We have listed the services that we offer to our clients, together with a brief description.</p>
  <div class="card help-card" style="left:78px">
    <svg width="48" height="48" viewBox="0 0 48 48" fill="none" stroke="#2d3a42" stroke-width="2.5"><rect x="6" y="4" width="26" height="34"/><line x1="11" y1="12" x2="27" y2="12"/><line x1="11" y1="18" x2="22" y2="18"/><circle cx="30" cy="28" r="8"/><line x1="36" y1="34" x2="44" y2="42"/></svg>
    <h3>Compilations</h3>
    <p>We view our role in the financial reporting process as an opportunity...</p>
    <div class="more">Know More</div>
  </div>
  <div class="card help-card" style="left:438px">
    <svg width="48" height="48" viewBox="0 0 48 48" fill="none" stroke="#2d3a42" stroke-width="2.5"><rect x="8" y="4" width="30" height="40" rx="3"/><text x="17" y="30" font-size="18" fill="#2d3a42" stroke="none" font-family="Arial">$</text></svg>
    <h3>Financial Statements</h3>
    <p>We can assist you in the preparation of your financial statements in...</p>
    <div class="more">Know More</div>
  </div>
  <div class="card help-card" style="left:798px">
    <svg width="48" height="48" viewBox="0 0 48 48" fill="none" stroke="#2d3a42" stroke-width="2.5"><rect x="8" y="4" width="30" height="40"/><line x1="14" y1="14" x2="32" y2="14"/><line x1="14" y1="22" x2="32" y2="22"/><line x1="14" y1="30" x2="26" y2="30"/></svg>
    <h3>Tax Advisory</h3>
    <p>Our team recognizes how difficult it is to stay up-to-date on the dynamic...</p>
    <div class="more">Know More</div>
  </div>
  <div class="dots" style="top:527px"><i class="on"></i><i></i><i></i></div>
</section>

<section class="about">
  <div class="about-img" role="img" aria-label="Photo of two businessmen reviewing documents at a laptop"></div>
  <div class="about-text">
    <h2>About <span>Us</span></h2>
    <p>At Lakeshore Ledger &amp; Office Partners, we work hard to realize our motto. We view every client relationship like a partnership, and truly believe that our success is a result of your success.</p>
    <p>We are committed to providing close, personal attention to our clients. We take pride in giving you the assurance that the assistance you receive comes from years of advanced training, technical experience and financial acumen. Our continual investment of time and resources in professional continuing education, advanced financial tools and extensive business relationships is indicative of our commitment to excellence.</p>
  </div>
</section>

<section class="alerts">
  <div class="h2">Tax <span>Alerts</span></div>
  <h3>AB - Provincial film and television grant program expanded</h3>
  <p>The government of Alberta has announced changes to its incentive programs for Alberta-based film and television productions, to adapt to changes in that industry. The new Screen-Based Production Gran...</p>
  <div class="dots" style="top:256px"><i class="on"></i><i></i><i></i></div>
</section>

<section class="quote">
  <div class="quote-img" role="img" aria-label="Photo of a businessman in a blue suit adjusting his jacket"></div>
  <h2>Request a <span>Quick Quote</span></h2>
  <p class="lead">Please feel free to contact us at the information provided below and we will be sure to get back to you as soon as possible.</p>
  <div class="field" style="left:78px;top:246px">Name</div>
  <div class="field" style="left:320px;top:246px">Phone No.</div>
  <div class="field" style="left:78px;top:306px">Email</div>
  <div class="field" style="left:320px;top:306px">Subject</div>
  <div class="submit">SUBMIT</div>
</section>

<section class="team">
  <div class="h2">Our <span>Team</span></div>
  <div class="card member" style="left:78px">
    <div class="member-img" role="img" aria-label="Portrait photo of team member"></div>
    <h3>Nadia Rahim</h3><hr>
    <p>Administrator and Business Development, Partner</p>
  </div>
  <div class="card member" style="left:438px">
    <div class="member-img" role="img" aria-label="Portrait photo of team member"></div>
    <h3>Omar Siddiq</h3><hr>
    <p>Senior Financial Advisor, Partner</p>
  </div>
  <div class="card member" style="left:798px">
    <div class="member-img" role="img" aria-label="Portrait photo of team member"></div>
    <h3>Sara Khalid</h3><hr>
    <p>Advertising and Marketing Manager</p>
  </div>
</section>

<section class="news">
  <div class="title" style="left:78px">Latest <span>News</span></div>
  <div class="title" style="left:799px">Keep <span>Up to Date</span></div>
  <div class="card post" style="left:78px">
    <h3>Blog Title</h3>
    <p>Lorem Ipsum is simply dummy text of the printing and typesetting industry.</p>
    <div class="meta"><span>by admin</span><span>12th April 2017</span></div>
  </div>
  <div class="card post" style="left:430px">
    <h3>Blog Title</h3>
    <p>Lorem Ipsum is simply dummy text of the printing and typesetting industry.</p>
    <div class="meta"><span>by admin</span><span>12th April 2017</span></div>
  </div>
  <div class="subscribe">
    <p>Subscribe to our newsletters to receive latest news and updates.</p>
    <div class="sub-field">Name</div>
    <div class="sub-field">Email
      <span class="sub-btn"><svg width="24" height="16" viewBox="0 0 24 16" fill="none" stroke="#fff" stroke-width="1.6"><rect x="1" y="1" width="22" height="14"/><polyline points="1,1 12,9 23,1"/></svg></span>
    </div>
  </div>
  <div class="dots" style="top:424px;justify-content:flex-start;padding-left:376px"><i class="on"></i><i></i></div>
</section>

<section class="map">
  <div class="abs" style="inset:0" role="img" aria-label="Street map of the office area"></div>
  <svg class="pin" width="44" height="60" viewBox="0 0 44 60"><path d="M22 58C22 58 4 34 4 20a18 18 0 0 1 36 0c0 14-18 38-18 38z" fill="#111"/><circle cx="22" cy="20" r="7" fill="#fff"/></svg>
  <div class="office">
    <h3>Main Office</h3>
    <ul>
      <li><svg width="14" height="18" viewBox="0 0 14 18"><path d="M7 17S1 10 1 6a6 6 0 0 1 12 0c0 4-6 11-6 11z" fill="#fff"/><circle cx="7" cy="6" r="2.2" fill="#2b2b2b"/></svg><span>Harbourview Place Suite 410-2210 98 Ave NW Edmonton,<br>AB T5J 0K4</span></li>
      <li><svg width="14" height="14" viewBox="0 0 14 14"><path d="M3 1l3 3-2 2a9 9 0 0 0 4 4l2-2 3 3-2 2C5 13 1 9 1 3z" fill="#fff"/></svg><span>Main Office: (587) 555 0142</span></li>
      <li><svg width="14" height="14" viewBox="0 0 14 14"><path d="M3 1l3 3-2 2a9 9 0 0 0 4 4l2-2 3 3-2 2C5 13 1 9 1 3z" fill="#fff"/></svg><span>Accounting Direct: (587) 555 0186</span></li>
      <li><svg width="14" height="12" viewBox="0 0 14 12" fill="none" stroke="#fff" stroke-width="1.4"><rect x="1" y="1" width="12" height="10"/><polyline points="1,1 7,6 13,1"/></svg><span>office@example.com</span></li>
    </ul>
  </div>
</section>

<footer class="site-footer">
  <nav class="foot-nav"><a>Home</a><a>About Us</a><a>Services</a><a>Newsletter</a><a>Financial Tools</a><a>Info Center</a><a>Contact</a></nav>
  <div class="social"><i></i><i></i><i></i></div>
  <div class="foot-line"></div>
  <div class="copy">© <b>Lakeshore Ledger</b> - 2017. All Rights Reserved.</div>
  <div class="to-top"><svg width="20" height="12" viewBox="0 0 20 12" fill="none" stroke="#fff" stroke-width="2.4"><polyline points="2,10 10,2 18,10"/></svg></div>
</footer>

</body>
</html>
```